Postcard Flyer For Plumbing Company

We are a p[professional plumbing company in NSW that carry out plumbing, electrical and hot water system work.
i want to send a postcard size flyer 105mm x 148mm to our clients to offer $xx off their next job they book with us.
The front of the flyer needs to say.... Feel The Love WIth $35 Off your Next Job. It needs to include a section where their name and postal address can go (74mm W x 24mm H) on the left hand side of the bottom of the flyer - refer attached example.
The other side of the flyer needs to have a section for text, the offer ($35 or $xx what they get off their next job) and also can use the tag line... Call 1 Number for The Best In 3 Trades - Plumbing, Hot Water & Electrical.
Plumbing, hot water and electrical pictures/icons can be used.
I want the flyer to stand out, use the corporate colours and be modern whilst letting them know that they can use this voucher on their next job.
Refer attachments.

Target Market(s)

Homeowners and our existing clients

Industry/Entity Type

Plumbing

Font styles to use
Serif

Colors
0255a3
ec1f27
ffffff
d3d3d3

Requirements
Must have
• Corporate colours and logos
• Red Colour:
• C=0
• M=100
• Y=100
• K=0
• Blue Colour
• C= 100
• M=66
• Y=0
• K=2
• Grey Colour
• C= 26
• M=21
• Y=19
• K=0
Nice to have
• predominately white background
Should not have
• Black background and lots of black.

```html
<!DOCTYPE html>
<html lang="en">
<head>
<meta charset="utf-8">
<title>Hale Contracting – $35 Off Postcard</title>
<link href="https://fonts.googleapis.com/css2?family=Anton&family=Oswald:wght@200;300;400;500;700&family=Arimo:wght@400;700&display=swap" rel="stylesheet">
<style>
  :root{
    --red:#d51f26;
    --red-bright:#ec1f27;
    --red-deep:#a8141a;
    --blue:#0255a3;
    --grey:#d3d3d3;
    --ink:#333333;
    --white:#ffffff;
  }
  html,body{margin:0;padding:0;overflow:hidden;}
  body{width:774px;height:1200px;position:relative;background:var(--white);font-family:"Arimo",Arial,sans-serif;}
  .face{position:absolute;left:0;width:774px;overflow:hidden;
    background:linear-gradient(120deg,#e6e6e6 0%,#f7f7f7 45%,#e2e2e2 100%);}
  .face--front{top:0;height:596px;}
  .face--back{top:600px;height:600px;}

  /* front */
  .top-rule{position:absolute;left:26px;top:69px;width:722px;height:3px;background:var(--red);}
  .banner{position:absolute;left:0;top:128px;width:774px;height:264px;
    background:linear-gradient(100deg,var(--red-deep) 0%,var(--red) 40%,#c11c22 70%,#b0181e 100%);}
  .banner-stripes{position:absolute;left:0;top:128px;}
  .web-pill{position:absolute;left:501px;top:106px;width:247px;height:41px;background:var(--blue);
    border-radius:10px 0 0 0;box-shadow:0 3px 0 #01356a;display:flex;align-items:center;gap:10px;
    padding-left:14px;box-sizing:border-box;color:var(--white);font-family:"Oswald",sans-serif;
    font-weight:300;font-size:20px;letter-spacing:2.5px;}
  .headline-love{position:absolute;left:28px;top:218px;margin:0;color:var(--white);white-space:nowrap;
    font-family:"Oswald",sans-serif;font-weight:200;font-size:71px;line-height:1;letter-spacing:3.4px;}
  .offer{position:absolute;left:0;top:0;color:var(--white);white-space:nowrap;}
  .offer span{position:absolute;line-height:1;}
  .offer-dollar{left:30px;top:300px;font-family:"Oswald",sans-serif;font-weight:300;font-size:28px;}
  .offer-amount{left:48px;top:302px;font-family:"Anton",sans-serif;font-size:96px;letter-spacing:-2px;}
  .offer-off{left:150px;top:310px;font-family:"Oswald",sans-serif;font-weight:300;font-style:italic;font-size:40px;}
  .offer-your{left:146px;top:348px;font-family:"Oswald",sans-serif;font-weight:700;font-style:italic;font-size:36px;}
  .offer-next{left:226px;top:290px;font-family:"Anton",sans-serif;font-size:106px;letter-spacing:-1px;
    transform-origin:0 0;transform:scaleX(1.22);}
  .offer-job{left:432px;top:392px;transform-origin:0 0;transform:rotate(-90deg);
    font-family:"Oswald",sans-serif;font-weight:300;font-size:80px;line-height:0.8 !important;letter-spacing:-2px;}

  .service-photos{position:absolute;left:27px;top:441px;display:flex;gap:9px;z-index:2;}
  .service-photo{width:108px;height:109px;box-shadow:0 3px 6px rgba(0,0,0,.35);border:1px solid #fff;}
  .service-photo--electrician{background:linear-gradient(135deg,#3d6fb6,#8fa5c0 60%,#c9cfd6);}
  .service-photo--trap{background:linear-gradient(135deg,#f3f3f3,#bdbdbd 55%,#e07050 80%,#e8e8e8);}
  .service-photo--tap{background:linear-gradient(135deg,#d8d8d8,#7c7c7c 50%,#2f2f2f);}
  .front-band{position:absolute;left:0;top:528px;}

  .brand{position:absolute;left:562px;width:200px;text-align:center;}
  .brand-name{font-family:"Oswald",sans-serif;font-weight:700;font-size:30px;line-height:1;color:var(--blue);}
  .brand-tag{margin-top:8px;font-family:"Arimo",Arial,sans-serif;font-weight:700;font-size:11.5px;color:var(--ink);white-space:nowrap;}
  .brand--front{top:485px;}
  .brand--back{top:489px;}

  /* back */
  .hero-photo{position:absolute;left:0;top:28px;}
  .tagline{margin:0;}
  .tagline span{position:absolute;left:29px;white-space:nowrap;font-family:"Oswald",sans-serif;line-height:1;}
  .tagline-call{top:61px;color:var(--blue);font-weight:700;font-size:55px;letter-spacing:0.3px;}
  .tagline-best{top:114px;color:var(--red-bright);font-weight:500;font-size:46px;letter-spacing:6px;}
  .tagline-trades{top:162px;color:var(--ink);font-weight:300;font-size:74px;letter-spacing:-2px;}
  .tagline-list{top:237px;color:var(--red-bright);font-weight:400;font-size:25px;letter-spacing:-0.5px;}

  .benefits{position:absolute;top:288px;margin:0;padding:0;list-style:none;width:310px;}
  .benefits--left{left:27px;}
  .benefits--right{left:430px;}
  .benefits li{position:relative;padding-left:23px;font-size:14.4px;line-height:14.5px;color:var(--ink);margin-bottom:5.8px;min-height:29px;}
  .benefits li svg{position:absolute;left:0;top:2px;}

  .back-band{position:absolute;left:0;top:488px;}
  .contact{position:absolute;left:27px;top:492px;margin:0;padding:0;list-style:none;color:var(--white);font-family:"Oswald",sans-serif;}
  .contact li{display:flex;align-items:center;height:29px;gap:12px;white-space:nowrap;}
  .contact svg{width:14px;flex:none;}
  .contact-address{font-size:15.5px;font-weight:400;}
  .contact-phone{font-size:19px;font-weight:500;}
  .contact-email{font-size:16.5px;font-weight:400;}
</style>
</head>
<body>

<section class="face face--front">
  <div class="top-rule"></div>
  <div class="banner" role="img" aria-label="Red-tinted photograph of chrome plumbing fittings and taps"></div>
  <svg class="banner-stripes" width="774" height="264" viewBox="0 0 774 264" aria-hidden="true">
    <polygon points="0,0 64,0 0,70" fill="#d9d9d9" opacity=".85"/>
    <polygon points="592,0 648,0 562,264 506,264" fill="#eeeeee" opacity=".9"/>
    <polygon points="690,0 774,0 774,60 706,264 618,264" fill="#e4e4e4" opacity=".85"/>
  </svg>
  <div class="web-pill">
    <svg width="16" height="16" viewBox="0 0 16 16" aria-hidden="true"><circle cx="8" cy="8" r="6.5" fill="none" stroke="#fff" stroke-width="1.4"/><ellipse cx="8" cy="8" rx="2.8" ry="6.5" fill="none" stroke="#fff" stroke-width="1.2"/><line x1="1.5" y1="8" x2="14.5" y2="8" stroke="#fff" stroke-width="1.2"/></svg>
    WWW.YOURWEB.COM
  </div>
  <h1 class="headline-love">Feelthe love With</h1>
  <div class="offer">
    <span class="offer-dollar">$</span>
    <span class="offer-amount">35</span>
    <span class="offer-off">off</span>
    <span class="offer-your">your</span>
    <span class="offer-next">NEXT</span>
    <span class="offer-job">JOB</span>
  </div>

  <svg class="front-band" width="486" height="68" viewBox="0 0 486 68" aria-hidden="true">
    <polygon points="0,0 416,0 486,68 0,68" fill="var(--red)"/>
  </svg>
  <div class="service-photos">
    <div class="service-photo service-photo--electrician" role="img" aria-label="Electrician in blue cap working at a switchboard"></div>
    <div class="service-photo service-photo--trap" role="img" aria-label="Hand tightening a sink trap with a red pipe wrench"></div>
    <div class="service-photo service-photo--tap" role="img" aria-label="Close-up of a chrome cross-handle tap"></div>
  </div>
  <div class="brand brand--front">
    <div class="brand-name">Hale<br>Contracting</div>
    <div class="brand-tag">Plumbing • Electrical • Hot Water</div>
  </div>
</section>

<section class="face face--back">
  <svg class="hero-photo" width="774" height="238" viewBox="0 0 774 238">
    <defs>
      <linearGradient id="heroTone" x1="0" y1="0" x2="1" y2="1">
        <stop offset="0" stop-color="#f4f4f4"/>
        <stop offset=".45" stop-color="#c4c4c4"/>
        <stop offset=".7" stop-color="#e8744e"/>
        <stop offset="1" stop-color="#7d8fb5"/>
      </linearGradient>
    </defs>
    <polygon points="416,0 450,0 364,238 350,238" fill="var(--red)"/>
    <polygon points="450,0 774,0 774,238 364,238" fill="url(#heroTone)" role="img" aria-label="Plumber's hands fitting a sink waste pipe with a red pipe wrench against white tiles"/>
  </svg>

  <h2 class="tagline">
    <span class="tagline-call">CALL 1 NUMBER</span>
    <span class="tagline-best">FOR THE BEST</span>
    <span class="tagline-trades">IN 3 TRADES</span>
    <span class="tagline-list">Plumbing, Hot Water &amp; Electrical.</span>
  </h2>

  <ul class="benefits benefits--left">
    <li><svg width="14" height="12" viewBox="0 0 14 12"><path d="M1 7 L5 11 L13 1" fill="none" stroke="var(--blue)" stroke-width="2.4"/></svg>Lorem ipsum dolor sit amet, consectetur adipiscing elit.</li>
    <li><svg width="14" height="12" viewBox="0 0 14 12"><path d="M1 7 L5 11 L13 1" fill="none" stroke="var(--blue)" stroke-width="2.4"/></svg>Sed eu libero vitae arcu tristique ornare nec ut augue.</li>
    <li><svg width="14" height="12" viewBox="0 0 14 12"><path d="M1 7 L5 11 L13 1" fill="none" stroke="var(--blue)" stroke-width="2.4"/></svg>Donec lobortis ligula vel diam condimentum interdum.</li>
    <li><svg width="14" height="12" viewBox="0 0 14 12"><path d="M1 7 L5 11 L13 1" fill="none" stroke="var(--blue)" stroke-width="2.4"/></svg>Phasellus vel ante vehicula, commodo odio ut, consequat tortor.</li>
    <li><svg width="14" height="12" viewBox="0 0 14 12"><path d="M1 7 L5 11 L13 1" fill="none" stroke="var(--blue)" stroke-width="2.4"/></svg>Integer nec quam quis purus porta lacinia et non libero.</li>
  </ul>
  <ul class="benefits benefits--right">
    <li><svg width="14" height="12" viewBox="0 0 14 12"><path d="M1 7 L5 11 L13 1" fill="none" stroke="var(--blue)" stroke-width="2.4"/></svg>Lorem ipsum dolor sit amet, consectetur adipiscing elit.</li>
    <li><svg width="14" height="12" viewBox="0 0 14 12"><path d="M1 7 L5 11 L13 1" fill="none" stroke="var(--blue)" stroke-width="2.4"/></svg>Sed eu libero vitae arcu tristique ornare nec ut augue.</li>
    <li><svg width="14" height="12" viewBox="0 0 14 12"><path d="M1 7 L5 11 L13 1" fill="none" stroke="var(--blue)" stroke-width="2.4"/></svg>Donec lobortis ligula vel diam condimentum interdum.</li>
    <li><svg width="14" height="12" viewBox="0 0 14 12"><path d="M1 7 L5 11 L13 1" fill="none" stroke="var(--blue)" stroke-width="2.4"/></svg>Phasellus vel ante vehicula, commodo odio ut, consequat tortor.</li>
    <li><svg width="14" height="12" viewBox="0 0 14 12"><path d="M1 7 L5 11 L13 1" fill="none" stroke="var(--blue)" stroke-width="2.4"/></svg>Integer nec quam quis purus porta lacinia et non libero.</li>
  </ul>

  <svg class="back-band" width="486" height="112" viewBox="0 0 486 112" aria-hidden="true">
    <polygon points="0,0 416,0 486,112 0,112" fill="var(--red)"/>
  </svg>
  <ul class="contact">
    <li class="contact-address"><svg viewBox="0 0 14 18" height="16"><path d="M7 1 A5.5 5.5 0 0 1 12.5 6.5 C12.5 10 7 17 7 17 C7 17 1.5 10 1.5 6.5 A5.5 5.5 0 0 1 7 1 Z" fill="none" stroke="#fff" stroke-width="1.6"/><circle cx="7" cy="6.5" r="2" fill="#fff"/></svg>123 Street Name, 22150 City Name, State (123456)</li>
    <li class="contact-phone"><svg viewBox="0 0 12 20" height="18"><rect x="1" y="1" width="10" height="18" rx="2" fill="none" stroke="#fff" stroke-width="1.6"/><rect x="3" y="4" width="6" height="5" fill="#fff"/><circle cx="6" cy="15" r="1.3" fill="#fff"/></svg>01234 56789</li>
    <li class="contact-email"><svg viewBox="0 0 16 11" height="11"><rect x="0.8" y="0.8" width="14.4" height="9.4" fill="#fff"/><path d="M1 1 L8 6.5 L15 1" fill="none" stroke="var(--red)" stroke-width="1.4"/></svg>info@yourmailhere.com</li>
  </ul>
  <div class="brand brand--back">
    <div class="brand-name">Hale<br>Contracting</div>
    <div class="brand-tag">Plumbing • Electrical • Hot Water</div>
  </div>
</section>

</body>
</html>
```